distributor of aftermarket auto electrical components

I am after business card design for my new company called
Summit Vehicle Supplies (SVS as the acronym). I will supplying automotive wiring components, basically from battery to headlight. I will be aiming to sell in the 4wd scene and to auto electricians. i am not worried which colours are used though i would like it to be dynamic.
Updates

sorry guys, i have add a mobile and e-mail address that will need to on there as well. Sorry for theĀ inconvenience.

sorry guys i had erred on my spelling with my e-mail. i have now fixed it in the brief

Target Market(s)

4wd industry, custom cars, RV, auto electricians

Industry/Entity Type

Electrical

Requirements
Must have
• Company Name
ABN number: 71 306 548 290
Director: Derek Holloway
M 0432 718 946
E dhollo@fernwire.com.au

```html
<!DOCTYPE html>
<html lang="en">
<head>
<meta charset="utf-8">
<title>Summit Vehicle Supplies – Business Card</title>
<link rel="stylesheet" href="https://fonts.googleapis.com/css2?family=Courier+Prime:wght@700&family=Playfair+Display:wght@700&display=swap">
<style>
  :root {
    --page-bg: #ffffff;
    --wood-dark: #8a5a2b;
    --wood-mid: #c08a52;
    --wood-light: #dcae78;
    --frame-edge: #5c3a18;
    --panel-deep: #0e7fa6;
    --panel-bright: #3fc4ea;
    --panel-dark: #0a3d5c;
    --band-white: #ffffff;
    --title-ink: #141a2e;
    --contact-ink: #ffffff;
    --contact-shadow: #0a0a0a;
  }
  html, body {
    margin: 0;
    padding: 0;
    width: 1200px;
    height: 742px;
    overflow: hidden;
    background: var(--page-bg);
  }
  .card {
    position: relative;
    width: 1200px;
    height: 742px;
  }
  .card__frame {
    position: absolute;
    inset: 0;
    box-sizing: border-box;
    border: 3px solid var(--frame-edge);
    border-radius: 10px;
    background: linear-gradient(160deg, var(--wood-light) 0%, var(--wood-mid) 45%, var(--wood-dark) 100%);
  }
  .card__panel {
    position: absolute;
    left: 52px;
    top: 12px;
    width: 1096px;
    height: 642px;
    background:
      radial-gradient(ellipse at 58% 62%, var(--panel-bright) 0%, var(--panel-deep) 55%, var(--panel-dark) 100%);
    box-shadow: inset 0 0 0 3px var(--frame-edge);
  }
  .card__band {
    position: absolute;
    left: 60px;
    top: 12px;
    width: 1080px;
    height: 170px;
    background: var(--band-white);
  }
  .card__title {
    position: absolute;
    left: 60px;
    top: 12px;
    width: 1080px;
    height: 170px;
    margin: 0;
    display: flex;
    align-items: center;
    justify-content: center;
    font-family: "Playfair Display", serif;
    font-weight: 700;
    font-size: 70px;
    color: var(--title-ink);
    letter-spacing: 1px;
  }
  .card__contact {
    position: absolute;
    left: 60px;
    top: 190px;
    width: 1080px;
    margin: 0;
    padding: 0;
    list-style: none;
    text-align: center;
    font-family: "Courier Prime", monospace;
    font-weight: 700;
    font-size: 46px;
    line-height: 92px;
    color: var(--contact-ink);
    text-shadow: 3px 3px 0 var(--contact-shadow), -1px -1px 0 var(--contact-shadow);
    letter-spacing: 2px;
  }
</style>
</head>
<body>
  <div class="card">
    <div class="card__frame"></div>
    <div class="card__panel" role="img" aria-label="Abstract cyan perspective tunnel of glowing panels"></div>
    <div class="card__band"></div>
    <h1 class="card__title">Summit Vehicle Supplies</h1>
    <ul class="card__contact">
      <li>ABN number: 71 306 548 290</li>
      <li>Director: Derek Holloway</li>
      <li>M 0432 718 946</li>
      <li>E dhollo@fernwire.com.au</li>
    </ul>
  </div>
</body>
</html>
```